occupational hygiene card design

We supply a service to the resource sector, commercial or government organisations to access health risks from physical or chemical hazards. We are a technical discipline that works within legislation.

Industry/Entity Type

Government

Contact Information for Business Card

KPLA
Kestrel plains occupational hygiene

```html
<!DOCTYPE html>
<html lang="en">
<head>
<meta charset="utf-8">
<title>KPLA Business Card</title>
<link rel="stylesheet" href="https://fonts.googleapis.com/css2?family=Open+Sans:wght@400;600;700&display=swap">
<style>
  :root {
    --brand-blue: #283a8f;
    --rule-blue: #2b3c9a;
    --ink: #1a1a1a;
    --card-white: #ffffff;
    --page: #f4f4f4;
  }
  * { margin: 0; padding: 0; box-sizing: border-box; }
  html, body { width: 1200px; height: 900px; overflow: hidden; }
  body {
    background: var(--page);
    font-family: "Open Sans", Arial, sans-serif;
    position: relative;
  }
  .card {
    position: absolute;
    width: 560px;
    height: 320px;
    overflow: hidden;
  }

  /* Front */
  .card-front {
    left: 560px; top: 80px;
    background: var(--card-white);
    border: 1px solid #e2e2e2;
  }
  .front-lockup { position: absolute; left: 26px; top: 22px; }
  .front-name {
    font-weight: 700;
    font-size: 88px;
    line-height: 1;
    letter-spacing: 2px;
    color: var(--brand-blue);
  }
  .front-rule { width: 300px; height: 3px; background: var(--ink); margin-top: 4px; }
  .front-tagline {
    font-size: 13.5px;
    color: var(--ink);
    letter-spacing: 0.4px;
    text-transform: uppercase;
    margin-top: 3px;
  }
  .line { position: absolute; background: var(--rule-blue); }
  .line-vertical { left: 390px; top: 0; width: 2px; height: 302px; }
  .line-mid { left: 0; top: 176px; width: 390px; height: 2px; }
  .line-name { left: 300px; top: 254px; width: 260px; height: 2px; }
  .holder {
    position: absolute; right: 36px; top: 226px; text-align: right;
    background: var(--card-white); padding-left: 8px;
  }
  .holder-name {
    font-weight: 700; font-size: 17px; color: var(--brand-blue);
    letter-spacing: 0.5px; text-transform: uppercase; line-height: 1.2;
    background: var(--card-white); display: inline-block; padding: 0 6px;
  }
  .holder-role { font-size: 12.5px; color: var(--ink); margin-top: 2px; }
  .contact-list { position: absolute; left: 26px; top: 232px; list-style: none; }
  .contact-list li {
    display: flex; align-items: center; gap: 8px;
    font-size: 13px; color: var(--ink); line-height: 20px;
  }
  .contact-list svg { width: 13px; height: 13px; flex: none; }
  .front-band { position: absolute; left: 0; bottom: 0; width: 100%; height: 18px; background: var(--brand-blue); }

  /* Back */
  .card-back { left: 120px; top: 480px; background: var(--brand-blue); }
  .back-lockup { position: absolute; left: 150px; top: 100px; color: var(--card-white); }
  .back-name { font-weight: 700; font-size: 76px; line-height: 1; letter-spacing: 2px; }
  .back-rule { width: 270px; height: 3px; background: var(--card-white); margin-top: 4px; }
  .back-tagline { font-size: 12px; letter-spacing: 0.4px; text-transform: uppercase; margin-top: 3px; }
</style>
</head>
<body>

<section class="card card-front" aria-label="Business card front">
  <div class="front-lockup">
    <div class="front-name">KPLA</div>
    <div class="front-rule"></div>
    <div class="front-tagline">Kestrel Plains Occupational Hygiene</div>
  </div>

  <div class="line line-vertical"></div>
  <div class="line line-mid"></div>
  <div class="line line-name"></div>

  <div class="holder">
    <div class="holder-name">Daniel Brooks</div>
    <div class="holder-role">Hygienist / Managing Director</div>
  </div>

  <ul class="contact-list">
    <li>
      <svg viewBox="0 0 14 14" aria-hidden="true"><circle cx="7" cy="7" r="7" fill="#283a8f"/><rect x="4.6" y="3" width="4.8" height="8" rx="0.8" fill="#fff"/><rect x="5.4" y="4" width="3.2" height="5" fill="#283a8f"/></svg>
      0412 555 018
    </li>
    <li>
      <svg viewBox="0 0 14 14" aria-hidden="true"><circle cx="7" cy="7" r="7" fill="#283a8f"/><rect x="3.5" y="4.5" width="7" height="5" fill="#fff"/><path d="M3.5 4.5 L7 7.3 L10.5 4.5" stroke="#283a8f" stroke-width="0.8" fill="none"/></svg>
      daniel.brooks@kpla.com.au
    </li>
    <li>
      <svg viewBox="0 0 14 14" aria-hidden="true"><circle cx="7" cy="7" r="7" fill="#283a8f"/><circle cx="7" cy="7" r="3.8" stroke="#fff" stroke-width="0.9" fill="none"/><ellipse cx="7" cy="7" rx="1.6" ry="3.8" stroke="#fff" stroke-width="0.8" fill="none"/><line x1="3.2" y1="7" x2="10.8" y2="7" stroke="#fff" stroke-width="0.8"/></svg>
      www.kpla.com.au
    </li>
  </ul>

  <div class="front-band"></div>
</section>

<section class="card card-back" aria-label="Business card back">
  <div class="back-lockup">
    <div class="back-name">KPLA</div>
    <div class="back-rule"></div>
    <div class="back-tagline">Kestrel Plains Occupational Hygiene</div>
  </div>
</section>

</body>
</html>
```